Vertical flyer design to guide people to my shop

We need a vertical flyer design for a tailor shop, Marlow Stitchworks. Our shop is on the 3/F, and we need this flyer/poster to placed on the G/F street level to guide people to take the lifts upstairs. Basically to tell people that, "We are here on 3/F!"

Dimensions ratio: 80 (wide) x200 (tall)

You may use the photos and graphics from the webpages below.
http://www.marlowstitchworks.net/en/marlow-stitchworks-hong-kong-tailors-tailor-shop/

https://www.cloth-q.com/tailor/marlow-stitchworks

```html
<!DOCTYPE html>
<html lang="en">
<head>
<meta charset="utf-8">
<title>Marlow Stitchworks – We Are Here on 3/F</title>
<link rel="stylesheet" href="https://fonts.googleapis.com/css2?family=Tinos:wght@400;700&family=Archivo+Black&family=Anton&display=swap">
<style>
  :root {
    --paper: #ffffff;
    --ink: #111111;
    --arrow-red: #a8232f;
    --ornament-light: #e4e4e4;
    --ornament-dark: #bdbdbd;
    --photo-red: #7d1a24;
    --photo-deep: #2b1418;
    --photo-blue: #4a5a8a;
    --roof-line: #1a1a1a;
  }
  html, body {
    margin: 0;
    padding: 0;
    overflow: hidden;
    background: var(--paper);
  }
  .flyer {
    position: relative;
    width: 1200px;
    height: 2764px;
    background: var(--paper);
    overflow: hidden;
  }
  .vine {
    position: absolute;
    top: 115px;
    width: 150px;
    height: 1570px;
    border-radius: 60px;
    background: linear-gradient(180deg, var(--ornament-light), var(--ornament-dark) 50%, var(--ornament-light));
  }
  .vine--left { left: 75px; }
  .vine--right { right: 75px; }
  .flourish {
    position: absolute;
    top: 705px;
    width: 200px;
    height: 70px;
    border-radius: 35px;
    background: linear-gradient(90deg, var(--ornament-dark), var(--ornament-light));
  }
  .flourish--left { left: 195px; }
  .flourish--right { right: 195px; transform: scaleX(-1); }
  .brand {
    position: absolute;
    top: 320px;
    left: 0;
    width: 100%;
    text-align: center;
    font-family: "Tinos", "Times New Roman", serif;
    color: var(--ink);
  }
  .brand__name {
    margin: 0;
    font-weight: 700;
    font-size: 100px;
    line-height: 112px;
    letter-spacing: 2px;
  }
  .brand__tagline {
    margin: 14px 0 0;
    font-weight: 400;
    font-size: 50px;
    line-height: 78px;
  }
  .lift-arrow {
    position: absolute;
    left: 370px;
    top: 715px;
    width: 460px;
    height: 510px;
  }
  .lift-arrow__label {
    position: absolute;
    left: 503px;
    top: 950px;
    width: 190px;
    text-align: center;
    font-family: "Tinos", "Times New Roman", serif;
    font-size: 30px;
    line-height: 55px;
    color: var(--paper);
  }
  .location {
    position: absolute;
    top: 1245px;
    left: 0;
    width: 100%;
    text-align: center;
    color: var(--ink);
  }
  .location__lead,
  .location__floor {
    margin: 0;
    font-family: "Archivo Black", "Arial Black", sans-serif;
    font-size: 96px;
    line-height: 110px;
  }
  .location__here {
    margin: 0;
    font-family: "Anton", "Impact", sans-serif;
    font-size: 250px;
    line-height: 236px;
  }
  .location__floor { font-size: 88px; line-height: 100px; }
  .workshop-photo {
    position: absolute;
    left: 0;
    top: 1730px;
    width: 1200px;
    height: 1010px;
  }
</style>
</head>
<body>
<main class="flyer">
  <div class="vine vine--left" role="img" aria-label="Black scrolling vine ornament running down the left side"></div>
  <div class="vine vine--right" role="img" aria-label="Black scrolling vine ornament running down the right side"></div>
  <div class="flourish flourish--left" role="img" aria-label="Small black scroll flourish"></div>
  <div class="flourish flourish--right" role="img" aria-label="Small black scroll flourish"></div>

  <header class="brand">
    <h1 class="brand__name">MARLOW<br>STITCHWORKS</h1>
    <p class="brand__tagline">EXPERT LADIES’<br>&amp; GENT’S TAILORS</p>
  </header>

  <svg class="lift-arrow" viewBox="0 0 460 510" aria-hidden="true">
    <polygon points="230,0 460,230 322,230 322,510 133,510 133,230 0,230" fill="var(--arrow-red)"/>
  </svg>
  <p class="lift-arrow__label">take<br>the lifts<br>upstairs</p>

  <section class="location">
    <p class="location__lead">we are</p>
    <p class="location__here">HERE</p>
    <p class="location__floor">on 3/F</p>
  </section>

  <svg class="workshop-photo" viewBox="0 0 1200 1010" role="img" aria-label="Photo of a roll of red tweed cloth, spools of thread and a tailor's hands cutting fabric with shears beside a measuring rule">
    <defs>
      <linearGradient id="workshopTones" x1="0" y1="0" x2="1" y2="1">
        <stop offset="0" stop-color="var(--photo-blue)"/>
        <stop offset="0.35" stop-color="var(--photo-red)"/>
        <stop offset="1" stop-color="var(--photo-deep)"/>
      </linearGradient>
    </defs>
    <polygon points="64,110 620,10 1136,110 1136,1000 64,1000" fill="url(#workshopTones)"/>
    <polyline points="64,110 620,10 1136,110" fill="none" stroke="var(--roof-line)" stroke-width="8"/>
  </svg>
</main>
</body>
</html>
```